Logo and website for new private wealth management business

This project is for a new company website and logo. The name of the firm is Harborline Estate Partners, LLC. We are a wealth management firm offering customized financial planning and investment management services to high net worth and ultra high net worth individuals and families. I want the website to feel contemporary but convey a feeling of sophistication and prestige.
www.tolvanridgeholdings.example and www.qnfunds.example are both good reference websites.
My clients will consist of wealthy individuals and families. I have existing clients in their 50s - 70s, but I also intend to target younger business owners and entrepreneurs in their 30s -50s.

Target Market(s)

Business owners, entrepreneurs and corporate executives. Many existing clients are in their 60s and 70s, but intend to also attract a younger clientele in their 30s - 50s.

Industry/Entity Type

Wealth management, investment advisory, financial planning

Coding

Coded - Design and coding required

Colors
0054AA
0677BA
7BADD7
CADEEF
E8F1F8
0094D4
00A9DD
6FCCEA
C7EBF8
E9F6FB
00AB8E
00BBA5
67D7C9
C6EFE9
E9F9F6
EE7325
F08F49
F5BC92
FAE3D3
FDF4ED

Requirements
Must have
• Should use blue as the main color theme. Should have an About, Services, Our Clients, FAQ, and Contact sections
Should not have
• Should not have pictures of people as the background.

```html
<!DOCTYPE html>
<html lang="en">
<head>
<meta charset="utf-8">
<title>Harborline Estate Partners, LLC</title>
<link href="https://fonts.googleapis.com/css2?family=Montserrat:wght@400;500;600;700&display=swap" rel="stylesheet">
<style>
:root{
  --blue:#0a84f0;
  --blue-bright:#1a8cff;
  --blue-deep:#0054aa;
  --navy:#133c78;
  --navy-dark:#0d2a57;
  --card:#1d4f8f;
  --ink:#1a1a1a;
  --text:#555;
  --line:#7badd7;
  --pale:#e8f1f8;
  --gold:#f5b301;
  --white:#fff;
}
*{box-sizing:border-box;margin:0;padding:0}
html,body{width:1200px;height:4093px;overflow:hidden}
body{position:relative;font-family:"Montserrat",sans-serif;color:var(--ink);background:var(--white)}
.abs{position:absolute}
.btn{position:absolute;display:flex;align-items:center;justify-content:center;background:var(--blue);color:#fff;font-size:14px;font-weight:600;border-radius:3px}
.eyebrow{position:absolute;font-size:14px;letter-spacing:1px;color:var(--blue);text-transform:uppercase}
.title{position:absolute;font-weight:700}
.rule{position:absolute;height:3px;width:40px;background:var(--blue)}
.vline{position:absolute;left:599px;width:1px;background:var(--line)}
.logo .name{font-weight:700;font-size:20px;color:#fff;letter-spacing:.5px;white-space:nowrap}
.logo .sub{font-size:11px;color:#fff;letter-spacing:6px;margin-top:4px;white-space:nowrap}

/* hero */
.hero-photo{left:0;top:0;width:1200px;height:540px;background:linear-gradient(180deg,#1f3f78 0%,#24518f 45%,#173a6e 75%,#0f2c58 100%)}
.top-nav{position:absolute;left:520px;top:32px;width:400px;height:20px;font-size:14px;color:#fff}
.top-nav span{position:absolute;top:0;white-space:nowrap}
.social-rail div{position:absolute;left:72px;width:24px;height:24px;display:flex;align-items:center;justify-content:center}
.hero-title{position:absolute;left:0;width:1200px;top:168px;text-align:center;color:#fff;font-size:31px;line-height:44px;font-weight:700;letter-spacing:.5px}
.hero-text{position:absolute;left:0;width:1200px;top:302px;text-align:center;color:#fff;font-size:16.5px;line-height:28px}

/* about */
.about-lead{left:454px;top:643px;width:580px;font-size:14.5px;font-weight:600;line-height:27px;color:#444}
.about-badge{left:160px;top:760px;width:252px;height:93px;background:var(--blue);color:#fff;padding:18px 0 0 20px;z-index:3}
.about-badge .name{font-size:22px}
.about-badge .sub{font-size:14px;letter-spacing:8px;margin-top:8px}
.about-frame{left:202px;top:758px;width:363px;height:410px;border:3px solid #9fc4ea}
.about-photo{left:208px;top:739px;width:351px;height:423px;background:linear-gradient(160deg,#e6eef7 0%,#a9c3df 35%,#4f6f97 70%,#1f3a60 100%)}
.about-body{left:618px;top:797px;width:412px;font-size:13px;line-height:24.5px;color:#555}

/* services */
.services{left:0;top:1115px;width:1200px;height:646px;background:linear-gradient(135deg,#0b7ef0 0%,#0a6fd6 50%,#0a5bb8 100%)}
.svc{position:absolute;top:1331px;width:204px;height:276px;background:var(--card);color:#fff;text-align:center;border-radius:2px}
.svc.alt{background:#2a5a96}
.svc svg{margin-top:40px}
.svc h3{font-size:14px;font-weight:600;margin-top:14px}
.svc p{font-size:11.5px;line-height:18px;color:#dde8f6;margin:18px 14px 0}
.svc .more{font-size:11.5px;color:var(--blue-bright);margin-top:6px}

/* testimonials */
.tcard{position:absolute;top:1950px;width:278px;height:270px;background:#fff;box-shadow:0 2px 10px rgba(0,0,0,.08);border-radius:4px;text-align:center}
.tcard.active{background:var(--card);color:#fff;border-radius:8px}
.tcard .stars{color:var(--gold);font-size:18px;letter-spacing:2px;margin-top:32px}
.tcard p{font-size:12.5px;line-height:21.5px;color:#444;margin:8px 24px 0}
.tcard.active p{color:#e5eef9}
.tcard hr{border:0;border-top:1px solid #e4e4e4;margin:18px 10px 0}
.tcard.active hr{border-top-color:#3d6aa6}
.tcard .who{font-size:14px;font-weight:600;margin-top:16px}
.arrow{position:absolute;top:2070px;width:31px;height:31px;border-radius:50%;display:flex;align-items:center;justify-content:center}

/* cta */
.cta{left:0;top:2388px;width:1200px;height:351px;background:linear-gradient(90deg,#1a8a9a 0%,#1c6ea6 45%,#1773c4 100%)}
.cta-title{position:absolute;left:0;width:1200px;top:2466px;text-align:center;color:#fff;font-size:26px;font-weight:700;letter-spacing:1px}
.cta-text{position:absolute;left:0;width:1200px;top:2511px;text-align:center;color:#fff;font-size:14px;line-height:26px}

/* faq */
.faq-bg{left:0;top:2780px;width:1200px;height:644px;background:linear-gradient(180deg,#fff 0%,#fff 40%,#eef0f2 70%,#e3e5e8 100%)}
.faq{position:absolute;left:251px;width:696px;background:#fff;border:1px solid #e4e4e4;box-shadow:0 1px 6px rgba(0,0,0,.05);font-size:14px;font-weight:600}
.faq .q{position:absolute;left:30px;top:15px}
.faq .sign{position:absolute;right:26px;top:12px;color:var(--blue);font-size:20px;font-weight:500}
.faq .a{position:absolute;left:30px;top:63px;width:640px;font-size:13.5px;font-weight:400;line-height:22px;color:#555;text-align:justify;letter-spacing:.6px}

/* contact */
.footer{left:0;top:3802px;width:1200px;height:291px;background:linear-gradient(180deg,#1b4c8c,#16407a)}
.copy{left:0;top:4033px;width:1200px;height:60px;background:var(--navy-dark);color:#c9d6ea;font-size:13px;display:flex;align-items:center;justify-content:center}
.contact-card{left:160px;top:3502px;width:878px;height:383px;background:#fff;box-shadow:0 3px 12px rgba(0,0,0,.08)}
.contact-side{left:674px;top:3502px;width:364px;height:383px;background:#0f62c0}
.field{position:absolute;border:1px solid #d6d6d6;border-radius:2px;font-size:11.5px;color:#777;padding:8px 10px}
.detail{position:absolute;left:702px;color:#fff;font-size:13px;display:flex;align-items:center;gap:12px;white-space:nowrap}
.ico{width:30px;height:30px;border:1.5px solid #fff;border-radius:50%;display:flex;align-items:center;justify-content:center;flex:none}
.dash{position:absolute;left:702px;width:300px;border-top:1px dashed #7badd7}
.foot-nav span{position:absolute;top:3952px;color:#fff;font-size:14px;white-space:nowrap}
.fsep{position:absolute;top:3950px;width:1px;height:20px;background:#4f75ad}
</style>
</head>
<body>

<!-- Hero -->
<section class="hero">
  <div class="abs hero-photo" role="img" aria-label="City skyline at dusk above a river and bridge, blue tones"></div>
  <div class="abs logo" style="left:160px;top:21px">
    <div class="name">Harborline Estate</div>
    <div class="sub" style="letter-spacing:5px">PARTNERS, LLC</div>
  </div>
  <nav class="top-nav">
    <span style="left:0">Home</span>
    <span style="left:73px">About</span>
    <span style="left:147px">Services</span>
    <span style="left:237px">Client Review</span>
    <span style="left:366px">FAQ</span>
  </nav>
  <div class="btn" style="left:949px;top:22px;width:89px;height:37px;font-weight:500;font-size:13px">Contact</div>

  <div class="social-rail">
    <div style="top:185px;background:var(--blue);border-radius:4px"><svg width="14" height="14" viewBox="0 0 14 14"><rect x="1" y="1" width="12" height="12" rx="3" fill="none" stroke="#fff" stroke-width="1.5"/></svg></div>
    <div style="top:226px"><svg width="10" height="10"><circle cx="5" cy="5" r="4" fill="#fff"/></svg></div>
    <div style="top:268px"><svg width="10" height="10"><circle cx="5" cy="5" r="4" fill="#fff"/></svg></div>
    <div style="top:309px"><svg width="10" height="10"><circle cx="5" cy="5" r="4" fill="#fff"/></svg></div>
  </div>

  <h1 class="hero-title">WEALTH MANAGEMENT FIRM<br>OFFERING CUSTOMIZED FINANCIAL<br>PLANNING..</h1>
  <p class="hero-text">Lorem ipsum dolor sit amet, consectetuer adipiscing elit, sed diam nonummy nibh<br>euismod tincidunt ut laoreet dolore magna aliquam erat volutpat</p>
  <div class="btn" style="left:531px;top:381px;width:138px;height:43px">Get Started</div>

  <svg class="abs" style="left:0;top:452px" width="1200" height="125" viewBox="0 0 1200 125">
    <path d="M0 10 C300 25 480 70 600 120 C720 70 900 25 1200 10 L1200 125 L0 125Z" fill="#1a86f0"/>
    <path d="M0 52 C300 70 480 95 600 120 C720 95 900 70 1200 52 L1200 125 L0 125Z" fill="#103f80"/>
    <path d="M0 62 C300 80 480 105 600 122 C720 105 900 80 1200 62 L1200 125 L0 125Z" fill="#fff"/>
  </svg>
  <div class="vline" style="top:524px;height:96px"></div>
</section>

<!-- About -->
<section class="about">
  <div class="eyebrow" style="left:160px;top:643px">Who we are</div>
  <div class="title" style="left:160px;top:665px;font-size:40px">About Us</div>
  <div class="rule" style="left:162px;top:713px"></div>
  <p class="abs about-lead">Dolor Sit Amet, Consectetuer Adipiscing Elit, Sed Diam Nonummy Nibh Euismod Tincidunt Ut Laoreet Dolore Magna Aliquam Erat Volutpat. Ut Wisi Enim Ad Minim Veniamtincidunt Ut Laoreet Dolore Magna Aliquam Erat Ut eet Dolore Magna Aliquam EratUt Laoreet Dolore Magna Aliquam..</p>
  <div class="abs about-frame"></div>
  <div class="abs about-photo" role="img" aria-label="Glass office towers seen from below against a bright sky"></div>
  <div class="abs about-badge logo">
    <div class="name">Harborline Estate</div>
    <div class="sub">PARTNERS, LLC</div>
  </div>
  <p class="abs about-body">Lorem ipsum dolor sit amet, consectetur adipiscing elit, sed do eiusmod tempor incididunt ut labore et dolore magna aliqua. Diam phasellus vestibulum lorem sed risus ultricies tristique. Aliquam purus sit amet luctus venenatis lectus magna fringilla urna. Viverra suspendisse potenti nullam ac tortor. Posuere ac ut consequat semper viverra venenatis lectus magna fringilla urna semper viverra venenatis lectus magna fringilla urna. .</p>
  <div class="btn" style="left:618px;top:1012px;width:138px;height:43px">Read More</div>
  <div class="vline" style="top:1073px;height:87px"></div>
</section>

<!-- Services -->
<section>
  <div class="abs services"></div>
  <div class="eyebrow" style="left:0;width:1200px;text-align:center;top:1216px;color:#dbe9fb">Who we are</div>
  <div class="title" style="left:0;width:1200px;text-align:center;top:1240px;font-size:35px;color:#fff">Our Services</div>
  <div class="rule" style="left:580px;top:1291px;background:#fff"></div>

  <div class="svc" style="left:160px">
    <svg width="64" height="60" viewBox="0 0 64 60" fill="none" stroke="#fff" stroke-width="2"><circle cx="32" cy="30" r="11"/><text x="32" y="35" font-size="13" fill="#fff" stroke="none" text-anchor="middle" font-family="Montserrat">$</text><path d="M6 58 V30 L14 18 L20 30 V42 L26 50"/><path d="M58 58 V30 L50 18 L44 30 V42 L38 50"/><path d="M32 6 V14 M26 10 L32 4 L38 10"/></svg>
    <h3>Wealth Management</h3>
    <p>Lorem ipsum dolor sit et, consectetur adipiscing elit, sed do eiusmod tempor incididunt ut labore et.</p>
    <div class="more">Learn more</div>
  </div>
  <div class="svc alt" style="left:386px">
    <h3 style="margin-top:38px;line-height:19px">Firm Offering<br>Customized</h3>
    <p style="margin-top:16px">Lorem ipsum dolor sit et, consectetur adipiscing elit, sed do eiusmod tempor incididunt ut labore et. m dolor sit et, consectetur adipiscing elit, sed do...</p>
    <div style="margin:14px auto 0;width:115px;height:35px;background:#fff;color:#1d4f8f;border-radius:3px;font-size:12px;display:flex;align-items:center;justify-content:center">Learn more</div>
  </div>
  <div class="svc" style="left:612px">
    <svg width="64" height="60" viewBox="0 0 64 60" fill="none" stroke="#fff" stroke-width="2"><rect x="8" y="4" width="30" height="40"/><text x="18" y="22" font-size="13" fill="#fff" stroke="none" font-family="Montserrat">$</text><path d="M14 30 H32 M14 36 H28"/><path d="M38 18 L54 4 M48 4 H54 V10" stroke="#3aa0ff"/><rect x="38" y="40" width="18" height="18"/><path d="M42 46 H52 M42 52 H52"/></svg>
    <h3>Financial Planning</h3>
    <p>Lorem ipsum dolor sit et, consectetur adipiscing elit, sed do eiusmod tempor incididunt ut labore et.</p>
    <div class="more">Learn more</div>
  </div>
  <div class="svc" style="left:834px">
    <svg width="64" height="60" viewBox="0 0 64 60" fill="none" stroke="#fff" stroke-width="2"><circle cx="32" cy="10" r="8"/><text x="32" y="15" font-size="11" fill="#fff" stroke="none" text-anchor="middle" font-family="Montserrat">$</text><path d="M6 10 H20 M16 6 L20 10 L16 14 M58 10 H44 M48 6 L44 10 L48 14"/><rect x="10" y="44" width="8" height="14"/><rect x="24" y="36" width="8" height="22"/><rect x="38" y="30" width="8" height="28"/><path d="M10 36 L24 26 L34 30 L52 18 M46 18 H52 V24"/></svg>
    <h3>Investment Management</h3>
    <p>Lorem ipsum dolor sit et, consectetur adipiscing elit, sed do eiusmod tempor incididunt ut labore et.</p>
    <div class="more">Learn more</div>
  </div>

  <div class="btn" style="left:531px;top:1645px;width:138px;height:43px;background:var(--blue-bright)">Contact Us</div>
  <div class="vline" style="left:606px;top:1761px;height:43px"></div>
</section>

<!-- Testimonials -->
<section>
  <div class="eyebrow" style="left:0;width:1200px;text-align:center;top:1849px">Who we are</div>
  <div class="title" style="left:0;width:1200px;text-align:center;top:1874px;font-size:35px">Client Testimonials.</div>
  <div class="rule" style="left:580px;top:1919px"></div>

  <div class="arrow" style="left:100px;border:1.5px solid #7badd7"><svg width="10" height="10" viewBox="0 0 10 10"><path d="M6.5 1.5 L3 5 L6.5 8.5" fill="none" stroke="#7badd7" stroke-width="1.5"/></svg></div>
  <div class="arrow" style="left:1067px;background:var(--blue)"><svg width="10" height="10" viewBox="0 0 10 10"><path d="M3.5 1.5 L7 5 L3.5 8.5" fill="none" stroke="#fff" stroke-width="1.5"/></svg></div>

  <div class="tcard" style="left:160px">
    <div class="stars">★★★★★</div>
    <p>"Lorem Pools has a wonderful team of real specialists. Last week they have built our new dream pool. We have been very impressed by their project manager and professional work teams. Thanks for super"</p>
    <hr><div class="who">Mara Ellison</div>
  </div>
  <div class="tcard active" style="left:461px">
    <div class="stars">★★★★★</div>
    <p>"Lorem Pools has a wonderful team of real specialists. Last week they have built our new dream pool. We have been very impressed by their project manager and professional work teams. Thanks for super"</p>
    <hr><div class="who">Dev Halloran</div>
  </div>
  <div class="tcard" style="left:761px">
    <div class="stars">★★★★★</div>
    <p>"Lorem Pools has a wonderful team of real specialists. Last week they have built our new dream pool. We have been very impressed by their project manager and professional work teams. Thanks for super"</p>
    <hr><div class="who">Owen Castell</div>
  </div>

  <div class="btn" style="left:531px;top:2261px;width:138px;height:45px">View All</div>
</section>

<!-- Call to action -->
<section>
  <div class="abs cta" role="img" aria-label="Soft teal and blue backdrop of an office setting"></div>
  <svg class="abs" style="left:272px;top:2423px" width="668" height="279">
    <g fill="none" stroke="#2fc3dc" stroke-width="3">
      <path d="M205 1.5 H1.5 V277.5 H205"/>
      <path d="M453 1.5 H666.5 V277.5 H453"/>
    </g>
  </svg>
  <h2 class="cta-title">LOREM IPSUM DOLOR SIT AMET</h2>
  <p class="cta-text">Lorem ipsum dolor sit amet, consectetur adipiscing elit, sed do eiusmod tempor<br>incididunt ut labore et dolor incididunt ut labore et dolorincididunte...</p>
  <div class="abs" style="left:494px;top:2578px;display:flex;align-items:center;gap:14px;color:#fff;font-size:17px;font-weight:600">
    <svg width="34" height="34" viewBox="0 0 34 34" fill="none" stroke="#fff" stroke-width="1.6"><circle cx="17" cy="17" r="15"/><path d="M11 10 L14 9 L16 14 L14 16 Q16 20 19 21 L21 19 L26 21 L25 24 Q18 26 12 19 Q9 14 11 10Z"/></svg>
    <span>(+1) 555, 014, 2290</span>
  </div>
  <div class="btn" style="left:532px;top:2625px;width:138px;height:45px">Get Started</div>
</section>

<!-- FAQ -->
<section>
  <div class="abs faq-bg" role="img" aria-label="Pale misty forest backdrop in light grey"></div>
  <div class="eyebrow" style="left:0;width:1200px;text-align:center;top:2828px">Who we are</div>
  <div class="title" style="left:0;width:1200px;text-align:center;top:2852px;font-size:35px">FAQ’s</div>
  <div class="rule" style="left:580px;top:2896px"></div>

  <div class="faq" style="top:2933px;height:147px;border-bottom:5px solid #0a6fd6">
    <span class="q">Lorem ipsum dolor sit amet, consectetuer</span><span class="sign">-</span>
    <div style="position:absolute;left:20px;right:20px;top:48px;border-top:1px solid #e8e8e8"></div>
    <p class="a">Lorem ipsum dolor sit amet, consectetuer adipiscing elit, sed diam nonummy nibh euismod tincidunt ut laoreet dolore magna aliquam erat volutpat. Ut wisi enim ad minim veniam, quis nostrud exerci tation &nbsp;ut aliquip ex ea commodo consequat.</p>
  </div>
  <div class="faq" style="top:3099px;height:50px"><span class="q">Lorem ipsum dolor sit amet, consectetuer</span><span class="sign">+</span></div>
  <div class="faq" style="top:3165px;height:50px"><span class="q">Lorem ipsum dolor sit amet, consectetuer</span><span class="sign">+</span></div>
  <div class="faq" style="top:3234px;height:50px"><span class="q">Lorem ipsum dolor sit amet, consectetuer</span><span class="sign">+</span></div>
  <div class="faq" style="top:3300px;height:50px"><span class="q">Lorem ipsum dolor sit amet, consectetuer</span><span class="sign">+</span></div>
  <div class="vline" style="top:3385px;height:84px"></div>
</section>

<!-- Contact and footer -->
<section>
  <div class="abs footer" role="img" aria-label="Dark blue city skyline backdrop"></div>
  <div class="abs contact-card"></div>
  <div class="abs contact-side"></div>

  <div class="title" style="left:160px;width:514px;text-align:center;top:3537px;font-size:26px">Contact Us</div>
  <div class="rule" style="left:386px;top:3576px;width:52px"></div>
  <div class="field" style="left:191px;top:3602px;width:216px;height:35px">First Name</div>
  <div class="field" style="left:424px;top:3602px;width:216px;height:35px">Last Name</div>
  <div class="field" style="left:191px;top:3655px;width:216px;height:35px">Phone No*</div>
  <div class="field" style="left:424px;top:3655px;width:216px;height:35px">Email*</div>
  <div class="field" style="left:191px;top:3707px;width:449px;height:73px">Message</div>
  <div class="btn" style="left:364px;top:3805px;width:105px;height:39px;font-size:13px">Submit</div>

  <div class="title" style="left:702px;top:3537px;font-size:26px;color:#fff">Contact Details</div>
  <div class="rule" style="left:703px;top:3576px;width:52px;background:#fff"></div>
  <div class="detail" style="top:3605px;align-items:flex-start;line-height:21px">
    <span class="ico"><svg width="12" height="14" viewBox="0 0 12 14" fill="none" stroke="#fff" stroke-width="1.4"><path d="M6 13 C2 8 1 6 1 5 A5 5 0 0 1 11 5 C11 6 10 8 6 13Z"/><circle cx="6" cy="5" r="1.6"/></svg></span>
    <span style="padding-top:1px">Halden Quay Offices<br>118 Alder Wharf Rd. Suite 4 Bayford,<br>CA 90000</span>
  </div>
  <div class="dash" style="top:3680px"></div>
  <div class="detail" style="top:3695px;font-size:17px;font-weight:600">
    <span class="ico"><svg width="14" height="14" viewBox="0 0 14 14" fill="none" stroke="#fff" stroke-width="1.4"><path d="M2 2 L5 1.5 L6.5 5 L5 6.5 Q6.5 9 8 9.5 L9.5 8 L13 9.5 L12.5 12.5 Q6 13 2.5 7 Q1 4 2 2Z"/></svg></span>
    <span>(+1) 555, 014, 2290</span>
  </div>
  <div class="dash" style="top:3744px"></div>
  <div class="detail" style="top:3759px">
    <span class="ico"><svg width="14" height="10" viewBox="0 0 14 10" fill="none" stroke="#fff" stroke-width="1.3"><rect x="1" y="1" width="12" height="8"/><path d="M1 1 L7 6 L13 1"/></svg></span>
    <span>info@harborline.example</span>
  </div>
  <div class="dash" style="top:3807px"></div>
  <div class="detail" style="top:3824px;gap:6px;font-size:12.5px">
    <span class="ico"><svg width="8" height="8"><circle cx="4" cy="4" r="3" fill="#fff"/></svg></span><span style="margin-right:8px">Newsroom</span>
    <span class="ico"><svg width="8" height="8"><circle cx="4" cy="4" r="3" fill="#fff"/></svg></span><span style="margin-right:8px">Updates</span>
    <span class="ico"><svg width="8" height="8"><circle cx="4" cy="4" r="3" fill="#fff"/></svg></span><span>Network</span>
  </div>

  <div class="abs logo" style="left:160px;top:3942px">
    <div class="name" style="font-size:24px">Harborline Estate</div>
    <div class="sub" style="font-size:13px;letter-spacing:7px;margin-top:6px">PARTNERS, LLC</div>
  </div>
  <nav class="foot-nav">
    <span style="left:541px">Home</span>
    <div class="fsep" style="left:601px"></div>
    <span style="left:614px">About</span>
    <div class="fsep" style="left:675px"></div>
    <span style="left:688px">Services</span>
    <div class="fsep" style="left:763px"></div>
    <span style="left:779px">Client Review</span>
    <div class="fsep" style="left:891px"></div>
    <span style="left:908px">FAQ</span>
    <div class="fsep" style="left:963px"></div>
    <span style="left:985px">Contact</span>
  </nav>
  <div class="abs copy">© 2022 Harborline Estate Partners. All Rights Reserved</div>
</section>

</body>
</html>
```